Homepage Real Estate Agency

I need a web design for a real estate agency in Luxembourg. A short draft for the front page can be found in the project details. (Page 1+2) The main colors of the site should be blue as shown in the project details. (Page 3)
The main target for this site is to promote real estates and a small presentation of the company.

Industry/Entity Type

Real Estate

Requirements
Must have
• On the front page estates are shown in a short preview in small boxes, on the right side is a search. The search is hidden except for the front page. The header has 4 buttons and the logo of the company.

```html
<!DOCTYPE html>
<html lang="en">
<head>
<meta charset="utf-8">
<title>Marlow Estates — Home</title>
<link rel="stylesheet" href="https://fonts.googleapis.com/css2?family=Gelasio:wght@400;700&display=swap">
<style>
  :root {
    --navy: #0b3d66;
    --navy-deep: #083457;
    --navy-text: #0d2f55;
    --sky: #1aa0d8;
    --sky-text: #1aa7dc;
    --red: #d3001c;
    --red-dark: #b8001a;
    --yellow: #f2e600;
    --paper: #ffffff;
    --mist: #efefef;
    --field-text: #4aa9d6;
  }
  * { box-sizing: border-box; margin: 0; padding: 0; }
  html, body { width: 914px; height: 1200px; overflow: hidden; }
  body {
    position: relative;
    background: var(--paper);
    font-family: "Gelasio", Georgia, serif;
    color: var(--navy-text);
  }
  .site-header {
    position: absolute; left: 0; top: 0; width: 914px; height: 112px;
    background: linear-gradient(180deg, #0a4674 0%, var(--navy-deep) 100%);
    box-shadow: 0 2px 4px rgba(0,0,0,.35);
    z-index: 2;
  }
  .brand {
    position: absolute; left: 0; top: 0; width: 128px; height: 112px;
    background: #083a62;
    box-shadow: 2px 0 6px rgba(0,0,0,.3);
    display: flex; flex-direction: column; align-items: center; justify-content: center; gap: 8px;
  }
  .brand-dot { width: 34px; height: 34px; border-radius: 50%; background: #2a36c8; }
  .brand-name { color: #fff; font-size: 13px; font-weight: 700; }
  .main-nav a {
    position: absolute; top: 0; height: 112px; padding-top: 74px;
    color: #fff; font-size: 13px; text-decoration: none; text-align: center;
  }
  .main-nav .is-active {
    background: #0a3a60; box-shadow: 0 0 6px rgba(0,0,0,.4);
  }
  .hero {
    position: absolute; left: 0; top: 112px; width: 914px; height: 276px;
    background: linear-gradient(90deg, #1487c4 0%, #1ea3dc 45%, #2bb0e4 75%, #1b8fc8 100%);
  }
  .hero-copy { position: absolute; left: 31px; top: 64px; width: 700px; color: #fff; }
  .hero-copy h1 { font-weight: 400; font-size: 26px; line-height: 33px; }
  .hero-copy p { margin-top: 16px; font-size: 15.5px; line-height: 19px; }
  .search {
    position: absolute; left: 0; top: 388px; width: 663px; height: 177px;
    background: linear-gradient(180deg, var(--red-dark) 0%, var(--red) 100%);
  }
  .search h2 { position: absolute; left: 18px; top: 23px; font-weight: 400; font-size: 17px; color: #fff; }
  .field {
    position: absolute; width: 259px; height: 26px; background: #fff;
    font-size: 10px; color: var(--field-text); padding: 7px 0 0 11px;
  }
  .field.is-filled { color: var(--navy-text); padding-left: 19px; }
  .field .calendar { position: absolute; right: 7px; top: 5px; }
  .tour-button {
    position: absolute; left: 18px; top: 132px; width: 127px; height: 29px;
    background: var(--yellow); border-radius: 3px; font-size: 11px; color: #222;
    padding: 8px 0 0 9px;
  }
  .options {
    position: absolute; left: 663px; top: 388px; width: 251px; height: 727px;
    background: radial-gradient(ellipse at 45% 50%, #ffffff 55%, #dcdcdc 100%);
  }
  .options h3 { position: absolute; left: 21px; top: 23px; font-size: 11px; font-weight: 400; color: #111; }
  .option { position: absolute; left: 24px; width: 200px; height: 78px; }
  .option-photo {
    position: absolute; left: 0; top: 0; width: 81px; height: 77px;
    background: linear-gradient(160deg, #c9ccd2 0%, #9ea3ab 55%, #6d727a 100%);
  }
  .option p { position: absolute; left: 93px; top: 14px; width: 110px; font-size: 10px; line-height: 12.5px; color: var(--navy-text); }
  .welcome { position: absolute; left: 18px; top: 598px; width: 600px; }
  .welcome h2 { font-weight: 400; font-size: 16px; color: var(--sky-text); }
  .welcome p { margin: 8px 0 0 3px; font-size: 10.2px; line-height: 12.4px; font-weight: 700; color: var(--navy-text); }
  .listing { position: absolute; width: 226px; }
  .listing-photo {
    width: 222px; height: 102px;
    background: linear-gradient(180deg, #f2e7c4 0%, #d7c08a 45%, #6d5a2e 80%, #3e3420 100%);
  }
  .listing h4 { margin-top: 13px; font-weight: 400; font-size: 11px; line-height: 12.5px; color: var(--navy-text); width: 210px; }
  .listing p { margin-top: 12px; font-size: 9.5px; line-height: 11.5px; color: var(--sky-text); }
  .site-footer {
    position: absolute; left: 0; top: 1128px; width: 914px; height: 72px; background: var(--mist);
  }
  .site-footer small { position: absolute; right: 33px; top: 27px; font-size: 10px; color: var(--navy-text); }
</style>
</head>
<body>
  <header class="site-header">
    <div class="brand"><span class="brand-dot"></span><span class="brand-name">Marlow Estates</span></div>
    <nav class="main-nav">
      <a class="is-active" href="#" style="left:507px;width:93px;">Home</a>
      <a href="#" style="left:606px;width:88px;">About Us</a>
      <a href="#" style="left:710px;width:78px;">Tour</a>
      <a href="#" style="left:808px;width:90px;">Contact Us</a>
    </nav>
  </header>

  <section class="hero" role="img" aria-label="Photo of a modern apartment building with trees, tinted blue">
    <div class="hero-copy">
      <h1>Lorem ipsum dolor sit amet, consectetur adipiscing elit. Praesent quis nibh massa, euismod interdum nibh. Donec vel dui sit amet lectus lacinia posuere.</h1>
      <p>Mauris semper ante sit amet metus dignissim sed aliquam mi scelerisque. In vestibulum, nibh vitae blandit tristique, enim felis malesuada ipsum, sed facilisis sapien lectus ac metus. Mauris vestibu-lum euismod mi, vel mollis lacus convallis in</p>
    </div>
  </section>

  <section class="search">
    <h2>Tell us what you are looking for?</h2>
    <div class="field" style="left:20px;top:56px;">how many rooms?</div>
    <div class="field" style="left:296px;top:56px;padding-left:20px;">schedule your time and date
      <svg class="calendar" width="17" height="15" viewBox="0 0 17 15" aria-hidden="true">
        <rect x="1" y="2" width="15" height="12" fill="none" stroke="#4aa9d6" stroke-width="1.4"/>
        <line x1="1" y1="5.5" x2="16" y2="5.5" stroke="#4aa9d6" stroke-width="1.4"/>
        <line x1="5" y1="0.5" x2="5" y2="3.5" stroke="#4aa9d6" stroke-width="1.4"/>
        <line x1="12" y1="0.5" x2="12" y2="3.5" stroke="#4aa9d6" stroke-width="1.4"/>
        <text x="8.5" y="12.8" font-size="7" text-anchor="middle" fill="#4aa9d6" font-family="Gelasio, serif">5</text>
      </svg>
    </div>
    <div class="field" style="left:20px;top:92px;">how many bathrooms?</div>
    <div class="field is-filled" style="left:296px;top:92px;">your budget</div>
    <div class="tour-button">get a tour of the place</div>
  </section>

  <aside class="options">
    <h3>Choose from the options below</h3>
    <div class="option" style="top:51px;"><div class="option-photo" role="img" aria-label="Photo of a bright living room with a white sofa"></div><p>"Neque porro quisquam est qui dolorem ipsum quia dolor sit amet, consectetur, adipisci velit..."</p></div>
    <div class="option" style="top:167px;"><div class="option-photo" role="img" aria-label="Photo of a bright living room with a white sofa"></div><p>"Neque porro quisquam est qui dolorem ipsum quia dolor sit amet, consectetur, adipisci velit..."</p></div>
    <div class="option" style="top:292px;"><div class="option-photo" role="img" aria-label="Photo of a bright living room with a white sofa"></div><p>"Neque porro quisquam est qui dolorem ipsum quia dolor sit amet, consectetur, adipisci velit..."</p></div>
    <div class="option" style="top:416px;"><div class="option-photo" role="img" aria-label="Photo of a bright living room with a white sofa"></div><p>"Neque porro quisquam est qui dolorem ipsum quia dolor sit amet, consectetur, adipisci velit..."</p></div>
    <div class="option" style="top:542px;"><div class="option-photo" role="img" aria-label="Photo of a bright living room with a white sofa"></div><p>"Neque porro quisquam est qui dolorem ipsum quia dolor sit amet, consectetur, adipisci velit..."</p></div>
  </aside>

  <section class="welcome">
    <h2>Welcome!</h2>
    <p>Lorem ipsum dolor sit amet, consectetur adipiscing elit. Praesent quis nibh massa, euismod interdum nibh. Donec vel dui sit amet lectus lacinia posuere. Mauris semper ante sit amet metus dignissim sed aliquam mi scelerisque. In vestibulum, nibh vitae blandit tristique, enim felis malesuada ipsum, sed facilisis sapien lectus ac metus. Mauris vestibulum euismod mi, vel mollis lacus convallis in. Phasellus in ipsum augue. Aenean et est lacus, vel ultrices diam. Aliquam erat volutpat. Cras arcu odio, hendrerit ac eleifend nec, pharetra eget magna.</p>
  </section>

  <article class="listing" style="left:65px;top:734px;">
    <div class="listing-photo" role="img" aria-label="Photo of a warmly lit lounge with wall lamps, sofa and vase"></div>
    <h4>Lorem ipsum dolor sit amet, consectetur adipiscing elit.</h4>
    <p>Praesent quis nibh massa, euismod interdum nibh. Donec vel dui sit amet lectus lacinia posuere.</p>
  </article>
  <article class="listing" style="left:369px;top:734px;">
    <div class="listing-photo" role="img" aria-label="Photo of a warmly lit lounge with wall lamps, sofa and vase"></div>
    <h4>Lorem ipsum dolor sit amet, consectetur adipiscing elit.</h4>
    <p>Praesent quis nibh massa, euismod interdum nibh. Donec vel dui sit amet lectus lacinia posuere.</p>
  </article>
  <article class="listing" style="left:65px;top:939px;">
    <div class="listing-photo" role="img" aria-label="Photo of a warmly lit lounge with wall lamps, sofa and vase"></div>
    <h4>Lorem ipsum dolor sit amet, consectetur adipiscing elit.</h4>
    <p>Praesent quis nibh massa, euismod interdum nibh. Donec vel dui sit amet lectus lacinia posuere.</p>
  </article>
  <article class="listing" style="left:369px;top:939px;">
    <div class="listing-photo" role="img" aria-label="Photo of a warmly lit lounge with wall lamps, sofa and vase"></div>
    <h4>Lorem ipsum dolor sit amet, consectetur adipiscing elit.</h4>
    <p>Praesent quis nibh massa, euismod interdum nibh. Donec vel dui sit amet lectus lacinia posuere.</p>
  </article>

  <footer class="site-footer">
    <small>© 2012 Marlow Estates</small>
  </footer>
</body>
</html>
```